Re-design existing website and add products for sale.

Our current website is very basic and cluttered. (emberfernwellness.com.au)We want a modern looking website that is easy to navigate. We also want to start selling essential oils and crystal products, so there needs to be a separate page for this. Also needs to be easily edited as we need to change the monthly oracle card with the description. Would like calming colours as we are all about natural healing. Alongside the services listed there should be a button to book now which asks for their name, email, phone number ect. and adds it to the cart.

• Logo is still being designed, please leave a space for the logo which will basically be a lotus flower within a mandala.

```html
<!DOCTYPE html>
<html lang="en">
<head>
<meta charset="utf-8">
<title>Ember Fern Wellness</title>
<link rel="stylesheet" href="https://fonts.googleapis.com/css2?family=Audiowide&family=Raleway:wght@400;500;600;700&family=Playfair+Display:wght@400&family=Kaushan+Script&display=swap">
<style>
:root{
  --pink:#e91e63;
  --pink-deep:#d8124f;
  --purple:#6a2c91;
  --ink:#1c1c1c;
  --text:#444;
  --light:#eef2f7;
  --navy:#0c3f66;
  --footer:#241e20;
  --white:#fff;
}
*{box-sizing:border-box;margin:0;padding:0}
html,body{width:1200px;height:3622px;overflow:hidden}
body{font-family:"Raleway",sans-serif;color:var(--text);background:var(--white);position:relative}
section,header,footer,nav{position:absolute;left:0;width:1200px}
.abs{position:absolute}
.fill{position:absolute}

/* header */
.site-header{top:0;height:89px;background:var(--white)}
.brand{left:234px;top:20px}
.brand-name{font-family:"Playfair Display",serif;color:var(--pink);font-size:27px;line-height:1}
.brand-tag{font-size:10px;color:#333;margin-top:4px}
.header-phone{left:655px;top:34px;font-size:11px;color:#555;display:flex;align-items:center;gap:6px}
.header-phone b{color:var(--ink)}
.btn{display:inline-flex;align-items:center;justify-content:center;background:var(--pink);color:var(--white);font-weight:700;text-transform:uppercase;font-size:11px;letter-spacing:.5px}
.header-book{left:811px;top:28px;width:98px;height:28px;border-radius:14px}
.header-cart{left:924px;top:29px}

.main-nav{top:89px;height:32px;background:var(--pink)}
.nav-links{position:absolute;left:234px;top:0;height:32px;display:flex;align-items:center}
.nav-links span{color:var(--white);font-size:10.5px;font-weight:600;margin-right:51px}
.social{position:absolute;display:flex;gap:12px}
.social i{display:block;width:18px;height:18px;border:2px solid var(--white);border-radius:50%}
.nav-social{left:843px;top:7px}

/* hero */
.hero{top:121px;height:531px;background:radial-gradient(ellipse at 50% 35%,#f6d88a 0%,#b9822f 30%,#5a3a16 62%,#2a1b0e 100%)}
.hero-center{position:absolute;left:0;width:1200px;text-align:center}
.label{display:inline-block;font-weight:700;color:var(--white);text-transform:uppercase;padding:3px 12px}
.hero-kicker{top:136px}
.hero-kicker .label{background:var(--pink);font-size:22px}
.hero-script{top:170px;font-family:"Kaushan Script",cursive;color:var(--white);font-size:44px}
.hero-name{top:266px}
.hero-name .label{background:var(--purple);font-size:22px}
.hero-role{top:305px;color:var(--white);font-size:22px}
.hero-book{left:516px;top:367px;width:169px;height:46px;font-size:13px}

/* welcome */
.welcome{top:652px;height:386px;background:var(--white)}
.welcome-kicker{left:234px;top:58px;font-size:20px;color:var(--ink);font-weight:500}
.welcome-title{left:234px;top:84px;font-family:"Audiowide",sans-serif;font-size:33px;color:var(--ink);line-height:1.05}
.welcome-text{left:234px;top:186px;width:345px;font-size:12.5px;line-height:1.75;color:#555}
.welcome-btn{left:234px;top:288px;width:150px;height:36px}
.welcome-photo{left:611px;top:0;width:589px;height:386px;background:linear-gradient(135deg,#c9c2ba,#8c8480 55%,#4e4852)}

/* services */
.services{top:1038px;height:478px;background:var(--light)}
.section-title{position:absolute;left:0;width:1200px;text-align:center;font-family:"Audiowide",sans-serif;font-size:33px;color:var(--ink)}
.title-rule{position:absolute;left:570px;width:60px;height:3px;background:var(--pink)}
.services .section-title{top:55px}
.services .title-rule{top:104px}
.service-grid{position:absolute;left:0;top:142px;width:1200px;height:208px;display:flex;gap:3px}
.service-tile{flex:1;position:relative}
.service-tile span{position:absolute;left:22px;bottom:22px;color:var(--white);font-size:14px}
.tile-reiki{background:linear-gradient(135deg,#f0ede9,#c6b6a8 60%,#7b6a5d)}
.tile-energy{background:linear-gradient(135deg,#c9c1a3,#8f8464 55%,#4c4736)}
.tile-chakra{background:linear-gradient(160deg,#e69735,#9b4a2a 50%,#2d2340)}
.tile-balance{background:linear-gradient(180deg,#6d7ea6,#c98a74 55%,#3c2f38)}
.services-btn{left:524px;top:378px;width:152px;height:36px;font-size:10px}

/* oracle */
.oracle{top:1516px;height:408px;background:linear-gradient(90deg,#c3184d 0%,var(--pink-deep) 40%,var(--pink-deep) 100%)}
.oracle-title{left:234px;top:62px;font-family:"Audiowide",sans-serif;font-size:31px;color:var(--white);line-height:1.05}
.oracle-deck{left:234px;top:146px;font-size:12px;color:var(--white);font-weight:700}
.oracle-card-name{left:234px;top:182px;font-size:12px;color:var(--white)}
.oracle-text{left:234px;top:212px;width:345px;font-size:12px;line-height:1.8;color:var(--white)}
.oracle-btn{left:234px;top:302px;width:152px;height:36px;background:var(--white);color:var(--pink)}
.oracle-frame{left:616px;top:42px;width:342px;height:352px;background:var(--white);border-radius:6px}
.oracle-month{left:616px;top:62px;width:342px;text-align:center;font-family:"Playfair Display",serif;font-size:19px;color:var(--pink);letter-spacing:1px}
.oracle-image{left:618px;top:89px;width:338px;height:230px;background:linear-gradient(135deg,#6b2a30,#33242e 50%,#1f3a4a)}

/* products */
.products{top:1924px;height:543px;background:var(--white)}
.products .section-title{top:55px}
.products .title-rule{top:104px}
.product-card{position:absolute;top:142px;width:357px;height:334px}
.product-card .caption{position:absolute;left:28px;bottom:28px;color:var(--white);font-size:20px;font-family:"Audiowide",sans-serif}
.product-card .view{position:absolute;right:28px;bottom:30px;color:var(--white);font-size:11px;font-weight:700;display:flex;gap:6px;align-items:center}
.product-oils{left:234px;background:linear-gradient(180deg,#dfe4ea,#6c7fa0 55%,#2a2f3a)}
.product-crystal{left:608px;background:linear-gradient(180deg,#e8e0d6,#b47a68 55%,#3c2e2a)}

/* testimonials */
.testimonials{top:2467px;height:466px;background:linear-gradient(90deg,#143a58,var(--navy) 40%,#0d4870)}
.testimonials .section-title{top:58px;color:var(--white);font-size:32px}
.testimonials .title-rule{top:107px}
.quote{position:absolute;top:150px;width:340px;color:var(--white)}
.quote-mark{font-family:"Playfair Display",serif;color:var(--pink);font-size:62px;line-height:.8;height:30px}
.quote p{font-size:13.5px;line-height:1.75;margin-top:12px}
.quote-author{display:flex;align-items:center;gap:12px;margin-top:28px}
.avatar{width:42px;height:42px;border-radius:50%;background:#b8c3cd}
.quote-author b{display:block;font-size:13px;font-weight:600}
.quote-author small{font-size:11px}
.q-left{left:252px}
.q-right{left:652px}
.arrow{position:absolute;top:268px}
.arrow-left{left:188px}
.arrow-right{left:972px}

/* map */
.map{top:2933px;height:314px;background:linear-gradient(160deg,#eceae4,#e2e6dd 60%,#cfe0d0)}
.map-pin{left:479px;top:96px;width:168px;height:62px;background:var(--pink);color:var(--white);text-align:center;font-size:11px;line-height:1.4;padding-top:8px}
.map-pin b{font-size:13px;font-weight:600;display:block}
.map-pin-tip{left:555px;top:158px}

/* footer */
.site-footer{top:3247px;height:375px;background:var(--footer);color:#ddd}
.news-title{left:234px;top:42px;font-size:11px;font-weight:700;color:var(--white);letter-spacing:.5px}
.news-sub{left:234px;top:72px;width:200px;font-size:10px;line-height:1.5;color:#ccc}
.news-input{left:451px;top:70px;width:240px;height:32px;background:var(--white);font-size:10px;color:#999;padding:9px 12px}
.news-btn{left:695px;top:70px;width:80px;height:32px}
.follow-title{left:830px;top:42px;font-size:11px;font-weight:700;color:var(--white)}
.footer-social{left:830px;top:70px}
.footer-brand{left:234px;top:150px}
.footer-brand .brand-tag{color:#ddd}
.col{position:absolute;top:146px;font-size:11px;line-height:1.7;color:#ddd}
.col h4{font-size:11px;font-weight:700;color:var(--white);margin-bottom:12px}
.col-contact{left:570px}
.col-products{left:733px}
.col-nav{left:858px}
.copyright{left:234px;top:318px;font-size:10.5px;color:#ccc}
.payments{left:762px;top:312px;display:flex;gap:6px}
.payments i{display:block;width:42px;height:24px;background:var(--white);border-radius:2px}
</style>
</head>
<body>

<header class="site-header">
  <div class="abs brand">
    <div class="brand-name">Ember Fern Wellness</div>
    <div class="brand-tag">Find Your True Self and Bring Balance to Your Life</div>
  </div>
  <div class="abs header-phone">
    <svg width="12" height="18" viewBox="0 0 12 18"><rect x="1" y="1" width="10" height="16" rx="2" fill="none" stroke="#e91e63" stroke-width="1.6"/><circle cx="6" cy="14" r="1" fill="#e91e63"/></svg>
    <span>CALL US: <b>0412 555 018</b></span>
  </div>
  <div class="abs btn header-book">Book Now</div>
  <svg class="abs header-cart" width="22" height="22" viewBox="0 0 22 22"><path d="M1 3h4l3 11h10l2-8H6" fill="none" stroke="#888" stroke-width="1.6"/><circle cx="9" cy="18" r="1.6" fill="#888"/><circle cx="16" cy="18" r="1.6" fill="#888"/><circle cx="18" cy="3" r="3" fill="#e91e63"/></svg>
</header>

<nav class="main-nav">
  <div class="nav-links"><span>HOME</span><span>ABOUT</span><span>SERVICES</span><span>PRODUCTS</span><span>CONTACT</span></div>
  <div class="social nav-social"><i></i><i></i><i></i><i></i></div>
</nav>

<section class="hero" role="img" aria-label="Glowing golden lotus of light on a dark background">
  <div class="hero-center hero-kicker"><span class="label">Find Your True Self and</span></div>
  <div class="hero-center hero-script">Bring Balance to Your Life</div>
  <div class="hero-center hero-name"><span class="label">Mira Castellan</span></div>
  <div class="hero-center hero-role">Reiki &amp; Seichim Master/Teacher/Practitioner</div>
  <div class="abs btn hero-book">Book Now</div>
</section>

<section class="welcome">
  <div class="abs welcome-kicker">WELCOME TO</div>
  <div class="abs welcome-title">EMBER FERN<br>WELLNESS</div>
  <p class="abs welcome-text">Are you struggling through life, feeling stuck, not feeling yourself, or simply feeling drained? Need to find a way to relax and rejuvenate, a way to free up your energy to work on that which better serves you in this lifetime?</p>
  <div class="abs btn welcome-btn">Learn More</div>
  <div class="fill welcome-photo" role="img" aria-label="Family portrait of the practitioner with her husband and two young sons"></div>
</section>

<section class="services">
  <h2 class="section-title">SERVICES WE OFFER</h2>
  <div class="title-rule"></div>
  <div class="service-grid">
    <div class="service-tile tile-reiki" role="img" aria-label="Hands giving a reiki healing"><span>Reiki &amp; Seichim Healings</span></div>
    <div class="service-tile tile-energy" role="img" aria-label="Hands reaching toward sunlight"><span>Energy Healing</span></div>
    <div class="service-tile tile-chakra" role="img" aria-label="Meditating figure with coloured chakra points at sunset"><span>Chakra Balancing</span></div>
    <div class="service-tile tile-balance" role="img" aria-label="Person meditating on a cliff at dusk"><span>Energy Balancing</span></div>
  </div>
  <div class="abs btn services-btn">More Services</div>
</section>

<section class="oracle">
  <div class="abs oracle-title">MONTHY<br>ORACLE CARD</div>
  <div class="abs oracle-deck">Threshold Oracle Cards (Ada Wren)</div>
  <div class="abs oracle-card-name">Morning Tide - "Gentle curiosity guides my day"</div>
  <p class="abs oracle-text">Welcome each new day with an open heart. Your lightness lifts the people near you, and as you let delight flow freely it ripples outward to touch all those around you.</p>
  <div class="abs btn oracle-btn">Learn More</div>
  <div class="abs oracle-frame"></div>
  <div class="abs oracle-month">FEBRUARY 2019</div>
  <div class="fill oracle-image" role="img" aria-label="Oracle card of the month laid on a woven cloth"></div>
</section>

<section class="products">
  <h2 class="section-title">OUR PRODUCTS</h2>
  <div class="title-rule"></div>
  <div class="product-card product-oils" role="img" aria-label="Row of blue essential oil roller bottles">
    <span class="caption">OILS</span>
    <span class="view">VIEW ALL <svg width="10" height="8" viewBox="0 0 10 8"><path d="M0 4h9M6 1l3 3-3 3" fill="none" stroke="#fff" stroke-width="1.4"/></svg></span>
  </div>
  <div class="product-card product-crystal" role="img" aria-label="Red and rose quartz crystal points">
    <span class="caption">CRYSTAL</span>
    <span class="view">VIEW ALL <svg width="10" height="8" viewBox="0 0 10 8"><path d="M0 4h9M6 1l3 3-3 3" fill="none" stroke="#fff" stroke-width="1.4"/></svg></span>
  </div>
</section>

<section class="testimonials" role="img" aria-label="Smiling woman in soft light behind a blue overlay">
  <h2 class="section-title">WHAT OUR CUSTOMERS ARE SAYING</h2>
  <div class="title-rule"></div>
  <svg class="arrow arrow-left" width="40" height="14" viewBox="0 0 40 14"><path d="M40 7H2M8 1L2 7l6 6" fill="none" stroke="#fff" stroke-width="1.5"/></svg>
  <div class="quote q-left">
    <div class="quote-mark">&ldquo;</div>
    <p>Lorem ipsum dolor sit amet, consectetur adipiscing elit, sed do eiusmod tempor incididunt ut labore et dolore magna aliqua. Ut enim ad minim veniam, quis nostrud exercitation ullamco laboris nisi ut aliquip ex ea commodo consequat.</p>
    <div class="quote-author"><span class="avatar"></span><div><b>Tom Brennan</b><small>Lorem ipsum dolor</small></div></div>
  </div>
  <div class="quote q-right">
    <div class="quote-mark">&ldquo;</div>
    <p>Lorem ipsum dolor sit amet, consectetur adipiscing elit, sed do eiusmod tempor incididunt ut labore et dolore magna aliqua. Ut enim ad minim veniam, quis nostrud exercitation ullamco laboris nisi ut aliquip ex ea commodo consequat.</p>
    <div class="quote-author"><span class="avatar"></span><div><b>Ruth Alder</b><small>Lorem ipsum dolor</small></div></div>
  </div>
  <svg class="arrow arrow-right" width="40" height="14" viewBox="0 0 40 14"><path d="M0 7h38M32 1l6 6-6 6" fill="none" stroke="#e91e63" stroke-width="1.5"/></svg>
</section>

<section class="map" role="img" aria-label="Street map of the surrounding suburb with a creek and wetlands">
  <div class="abs map-pin"><b>Ember Fern Wellness</b>42 Wattle Lane<br>Seaview, SA 5099</div>
  <svg class="abs map-pin-tip" width="16" height="10" viewBox="0 0 16 10"><path d="M0 0h16L8 10z" fill="#e91e63"/></svg>
</section>

<footer class="site-footer">
  <div class="abs news-title">SUBSCRIBE TO OUR NEWSLETTER TODAY:</div>
  <div class="abs news-sub">Do you want to know everything about our latest products and promotions?</div>
  <div class="abs news-input">Email Address</div>
  <div class="abs btn news-btn">Join</div>
  <div class="abs follow-title">FOLLOW US</div>
  <div class="social footer-social"><i></i><i></i><i></i><i></i></div>

  <div class="abs brand footer-brand">
    <div class="brand-name">Ember Fern Wellness</div>
    <div class="brand-tag">Find Your True Self and Bring Balance to Your Life</div>
  </div>
  <div class="col col-contact">
    <h4>GET IN TOUCH</h4>
    42 Wattle Lane<br>Seaview, SA 5099<br><br>P: 0412 555 018<br>E: hello@emberfernwellness.com.au
  </div>
  <div class="col col-products">
    <h4>PRODUCTS</h4>
    Oils<br>Crystal
  </div>
  <div class="col col-nav">
    <h4>NAVIGATION</h4>
    Home<br>About<br>Services<br>Products<br>Contact
  </div>
  <div class="abs copyright">&copy; 2019 Ember Fern Wellness. All Rights Reserved.</div>
  <div class="abs payments"><i></i><i></i><i></i><i></i><i></i></div>
</footer>

</body>
</html>
```